We need a web page design for a new company called "Brindle". We provide an innovative music sharing mobile application that allows music listeners to share their music without paying for a monthly subscription. We would like to incorporate the attached logo and color scheme. The final design should communicate music gifting and sharing.

Industry/Entity Type

It Company

```html
<!DOCTYPE html>
<html lang="en">
<head>
<meta charset="utf-8">
<title>Brindle – Music Sharing Mobile Application</title>
<link href="https://fonts.googleapis.com/css2?family=Lato:ital,wght@0,300;0,400;0,700;0,900;1,400;1,700&display=swap" rel="stylesheet">
<style>
  :root {
    --green: #5fa70a;
    --navy: #1b2431;
    --mist: #eceff1;
    --white: #ffffff;
    --ink: #4a5561;
    --ink-soft: #8b949c;
    --heading: #3b4652;
    --body-blue: #8c9bb5;
    --line: #d5d9dc;
  }
  * { box-sizing: border-box; margin: 0; padding: 0; }
  html, body { width: 708px; height: 1200px; overflow: hidden; }
  body { font-family: "Lato", sans-serif; background: var(--white); position: relative; color: var(--ink); }
  .backdrop { position: absolute; inset: 0; }
  .abs { position: absolute; }

  .site-header { position: absolute; top: 0; left: 0; width: 708px; height: 44px; background: var(--green); }
  .brand { position: absolute; left: 80px; top: 9px; display: flex; align-items: center; gap: 6px; color: var(--white); font-weight: 900; font-size: 22px; line-height: 26px; }
  .brand-dot { width: 20px; height: 20px; border-radius: 50%; background: var(--white); }
  .nav-link { position: absolute; top: 12px; height: 21px; line-height: 19px; color: var(--white); text-decoration: none; font-size: 11px; font-weight: 700; white-space: nowrap; border: 1px solid transparent; }
  .nav-link.active { border-color: var(--white); width: 51px; text-align: center; }

  .hero-title { left: 78px; top: 109px; color: var(--white); white-space: nowrap; }
  .hero-title h1 { font-size: 22px; font-weight: 900; letter-spacing: .3px; line-height: 26px; }
  .hero-title p { font-size: 17px; font-weight: 400; line-height: 24px; margin-top: 1px; }
  .hero-copy { left: 78px; top: 193px; width: 205px; font-size: 7.6px; line-height: 12.5px; color: var(--body-blue); }
  .btn-outline { left: 78px; top: 253px; width: 75px; height: 22px; border: 1px solid var(--green); color: var(--green); font-size: 7.5px; font-weight: 700; display: flex; align-items: center; justify-content: center; }

  .stat { right: 290px; text-align: right; white-space: nowrap; }
  .stat strong { display: block; font-size: 14px; font-weight: 900; color: var(--navy); line-height: 13px; }
  .stat span { display: block; font-size: 6.5px; line-height: 9px; color: var(--ink-soft); letter-spacing: .3px; }
  .stat-mark { width: 16px; height: 16px; border-radius: 50%; background: var(--green); }

  .device-phone { left: 488px; top: 78px; width: 120px; height: 312px; border-radius: 18px; background: linear-gradient(160deg,#f4f5f6,#c9cdd1); }
  .device-tablet { left: 106px; top: 518px; width: 182px; height: 100px; border-radius: 8px; background: linear-gradient(165deg,#f2f3f4,#6e5a7c); transform: skewY(-8deg); }

  .section-title { font-size: 16px; color: var(--heading); font-weight: 400; letter-spacing: .3px; line-height: 20px; }
  .section-title b { font-weight: 900; }
  .features-head { left: 292px; top: 429px; width: 340px; text-align: center; }
  .features-head p { font-size: 9.5px; line-height: 14.5px; color: var(--ink-soft); margin-top: 4px; }
  .feature { width: 138px; }
  .feature.left { text-align: right; }
  .feature h3 { font-size: 9px; font-weight: 700; color: var(--heading); margin-top: 3px; white-space: nowrap; }
  .feature p { font-size: 6.8px; line-height: 10.5px; color: var(--ink-soft); margin-top: 5px; }
  .feature svg { display: inline-block; }

  .reviews { left: 100px; top: 694px; width: 280px; text-align: center; }
  .reviews .lead { font-size: 9.5px; color: var(--ink-soft); margin-top: 6px; }
  .quote { font-size: 8.6px; line-height: 12.5px; font-style: italic; color: var(--ink-soft); }
  .quote b { color: var(--heading); }
  .reviewer { font-size: 8px; font-weight: 700; color: var(--heading); line-height: 12px; }
  .reviewer-photo { left: 542px; top: 744px; width: 88px; height: 88px; border-radius: 50%; border: 3px solid var(--white); background: linear-gradient(160deg,#f0d9a8,#c9b6a7); }
  .pager { left: 578px; top: 721px; color: var(--white); font-weight: 900; font-size: 15px; letter-spacing: 4px; }

  .contact { left: 79px; top: 924px; width: 180px; }
  .contact .lead { width: 155px; font-size: 9.5px; line-height: 14.5px; color: var(--ink-soft); margin-top: 6px; }
  .field { border-bottom: 1px solid var(--line); font-size: 8px; color: var(--ink); height: 24px; padding-top: 9px; }
  .btn-send { left: 78px; top: 1127px; width: 82px; height: 22px; border: 1px solid var(--line); color: var(--ink-soft); font-size: 7.5px; display: flex; align-items: center; justify-content: center; }

  .info { left: 412px; width: 180px; text-align: center; color: var(--white); }
  .info h4 { font-size: 9.5px; font-style: italic; font-weight: 700; margin-top: 4px; }
  .info p { font-size: 9.5px; margin-top: 4px; line-height: 12px; }
  .info-small p { font-size: 8.3px; font-style: italic; }

  .site-footer { position: absolute; left: 0; top: 1175px; width: 708px; height: 25px; background: var(--green); color: var(--white); font-size: 7.5px; display: flex; align-items: center; justify-content: center; gap: 6px; }
  .social { width: 16px; height: 16px; border-radius: 50%; background: var(--white); }
</style>
</head>
<body>

<svg class="backdrop" width="708" height="1200" viewBox="0 0 708 1200" aria-hidden="true">
  <polygon points="0,44 520,44 133,390 105,372 0,470" fill="var(--navy)"/>
  <polygon points="0,470 105,372 630,643 335,930 130,838 0,905" fill="var(--mist)"/>
  <polygon points="630,643 708,690 708,985 505,860 398,965 335,930" fill="var(--green)"/>
  <polygon points="505,860 708,985 708,1175 175,1175" fill="var(--navy)"/>
  <path d="M422,282 q6,0 6,6 v4 q0,4 4,4 q-4,0 -4,4 v4 q0,6 -6,6" fill="none" stroke="#c5c9cd"/>
  <path d="M422,322 q6,0 6,6 v4 q0,4 4,4 q-4,0 -4,4 v4 q0,6 -6,6" fill="none" stroke="#c5c9cd"/>
  <path d="M422,362 q6,0 6,6 v4 q0,4 4,4 q-4,0 -4,4 v4 q0,6 -6,6" fill="none" stroke="#c5c9cd"/>
  <path d="M244,510 q10,-30 52,-31" fill="none" stroke="#4a5561" stroke-width="1"/>
  <path d="M290,474 l7,5 l-8,3" fill="none" stroke="#4a5561"/>
  <path d="M522,770 q-20,-35 -58,-28" fill="none" stroke="#4a5561" stroke-width="1"/>
  <path d="M470,737 l-7,5 l8,4" fill="none" stroke="#4a5561"/>
  <line x1="460" y1="492" x2="460" y2="646" stroke="var(--line)"/>
  <line x1="308" y1="569" x2="615" y2="569" stroke="var(--line)"/>
  <text x="240" y="768" text-anchor="middle" font-family="Georgia, serif" font-size="30" font-weight="700" fill="var(--green)">&#8220;</text>
  <circle cx="240" cy="829" r="3.5" fill="none" stroke="#4a5561"/>
</svg>

<header class="site-header">
  <div class="brand"><span class="brand-dot"></span>Brindle</div>
  <nav>
    <a class="nav-link active" style="left:241px">Home</a>
    <a class="nav-link" style="left:306px">About Us</a>
    <a class="nav-link" style="left:372px">Features</a>
    <a class="nav-link" style="left:437px">How It Works</a>
    <a class="nav-link" style="left:524px">Download</a>
    <a class="nav-link" style="left:595px">Contact</a>
  </nav>
</header>

<section>
  <div class="abs hero-title">
    <h1>A BRINDLE APP</h1>
    <p>MUSIC SHARING MOBILE<br>APPLICATION</p>
  </div>
  <p class="abs hero-copy">Lorem ipsum dolor sit amet, consectetur adipiscing elit. Pellentesque sed finibus lectus. Ut in sapien id n rutrum lacinia id nec tellus. Etiam tempor leo eu vulputa auctor. In feugiat sollicitudin enim sit amet volutpat.</p>
  <div class="abs btn-outline">GET APP NOW</div>

  <div class="abs stat" style="top:283px"><strong>6220</strong><span>DOWNLOADS</span></div>
  <div class="abs stat-mark" style="left:438px;top:285px"></div>
  <div class="abs stat" style="top:324px"><strong>254</strong><span>MOBILE USER</span></div>
  <div class="abs stat-mark" style="left:438px;top:326px"></div>
  <div class="abs stat" style="top:366px"><strong>738</strong><span>TABLET USER</span></div>
  <div class="abs stat-mark" style="left:438px;top:367px"></div>

  <div class="abs device-phone" role="img" aria-label="Phone showing the Brindle app login screen"></div>
</section>

<section>
  <div class="abs device-tablet" role="img" aria-label="Tablet showing the Brindle music player"></div>
  <div class="abs features-head">
    <h2 class="section-title"><b>AWESOME</b> FEATURES</h2>
    <p>Lorem ipsum dolor sit amet, consectetur adipiscing elit. Vivamus tristique a massa vitae egestas. Phasellus posuere sit amet tellus vitae.</p>
  </div>

  <div class="abs feature left" style="left:309px;top:494px">
    <svg width="20" height="20" viewBox="0 0 20 20"><path d="M3,12 v-2 a7,7 0 0 1 14,0 v2" fill="none" stroke="var(--green)" stroke-width="2.2"/><rect x="2" y="11" width="4" height="7" rx="1.5" fill="var(--green)"/><rect x="14" y="11" width="4" height="7" rx="1.5" fill="var(--green)"/></svg>
    <h3>ALL SONGS AVAILABLE</h3><p>Ut labores laoreet petentium vix. Nec cu eripuit alterum, vel cibo laoree</p>
  </div>
  <div class="abs feature" style="left:471px;top:494px">
    <svg width="20" height="20" viewBox="0 0 20 20"><path d="M3,12 v-2 a7,7 0 0 1 14,0 v2" fill="none" stroke="var(--green)" stroke-width="2.2"/><rect x="2" y="11" width="4" height="7" rx="1.5" fill="var(--green)"/><rect x="14" y="11" width="4" height="7" rx="1.5" fill="var(--green)"/></svg>
    <h3>SHARE MUSIC ANYTIME</h3><p>Ut labores laoreet petentium vix. Nec cu eripuit alterum, vel cibo laoree</p>
  </div>
  <div class="abs feature left" style="left:309px;top:579px">
    <svg width="20" height="20" viewBox="0 0 20 20"><path d="M3,12 v-2 a7,7 0 0 1 14,0 v2" fill="none" stroke="var(--green)" stroke-width="2.2"/><rect x="2" y="11" width="4" height="7" rx="1.5" fill="var(--green)"/><rect x="14" y="11" width="4" height="7" rx="1.5" fill="var(--green)"/></svg>
    <h3>ON MONTHLY CHARGE</h3><p>Ut labores laoreet petentium vix. Nec cu eripuit alterum, vel cibo laoree</p>
  </div>
  <div class="abs feature" style="left:471px;top:579px">
    <svg width="20" height="20" viewBox="0 0 20 20"><path d="M3,12 v-2 a7,7 0 0 1 14,0 v2" fill="none" stroke="var(--green)" stroke-width="2.2"/><rect x="2" y="11" width="4" height="7" rx="1.5" fill="var(--green)"/><rect x="14" y="11" width="4" height="7" rx="1.5" fill="var(--green)"/></svg>
    <h3>USER FRIENDLY</h3><p>Ut labores laoreet petentium vix. Nec cu eripuit alterum, vel cibo laoree</p>
  </div>
</section>

<section>
  <div class="abs reviews">
    <h2 class="section-title"><b>APP</b> REVIEWS</h2>
    <p class="lead">Hear what our customer have to say...</p>
  </div>
  <p class="abs quote" style="left:100px;top:770px;width:280px;text-align:center">Lorem ipsum dolor sit amet, consectetur adipiscing elit. Nulla venenatis hendrerit massa at posuere. Donec eu consectetur felis. Cum sociis natoque penatibus et magnis dis parturient montes, nascetur ridiculus mus. Sed tincidunt est vel dolor tristique, <b>eu rhoncus mi ornare.</b></p>
  <p class="abs reviewer" style="left:100px;top:839px;width:280px;text-align:center">MARISSA HOLT<br>NORTHVALE INC</p>
  <div class="abs pager">&lt; &gt;</div>
  <div class="abs reviewer-photo" role="img" aria-label="Portrait of the reviewer"></div>
</section>

<section>
  <div class="abs contact">
    <h2 class="section-title"><b>CONTACT</b> US</h2>
    <p class="lead">Let drop a line to us &amp; we will be in touch soon.</p>
    <div class="field" style="margin-top:4px">NAME</div>
    <div class="field" style="margin-top:5px">EMAIL</div>
    <div class="field" style="margin-top:3px">MESSAGE</div>
    <div class="field"></div>
    <div class="field"></div>
  </div>
  <div class="abs btn-send">SEND MESSAGE</div>

  <div class="abs info" style="top:933px">
    <svg width="12" height="12" viewBox="0 0 12 12"><path d="M2,1 l3,0 l1,3 l-1.5,1 a7,7 0 0 0 3,3 l1,-1.5 l3,1 l0,3 a10,10 0 0 1 -9.5,-9.5z" fill="var(--green)"/></svg>
    <h4>Phone</h4><p>1.555.014270</p>
  </div>
  <div class="abs info" style="top:1003px">
    <svg width="14" height="11" viewBox="0 0 14 11"><rect width="14" height="11" rx="1" fill="var(--green)"/><path d="M1,1 l6,5 l6,-5" fill="none" stroke="var(--navy)" stroke-width="1.2"/></svg>
    <h4>Email</h4><p>info@brindleapp.com</p>
  </div>
  <div class="abs info info-small" style="top:1071px">
    <svg width="11" height="14" viewBox="0 0 11 14"><path d="M5.5,14 c-3,-4 -5.5,-6.5 -5.5,-8.5 a5.5,5.5 0 0 1 11,0 c0,2 -2.5,4.5 -5.5,8.5z" fill="var(--green)"/><circle cx="5.5" cy="5.5" r="2" fill="var(--navy)"/></svg>
    <h4>Location</h4><p>Street no. 453, Area name, Country name<br>Country code 123.456.</p>
  </div>
</section>

<footer class="site-footer">
  <span>© 2014 Brindle Share The Sound. All Rights Reserved</span>
  <span class="social"></span><span class="social"></span><span class="social"></span>
</footer>

</body>
</html>
```